New Business Card Design Project

We are a Nationally ranked independent premium furniture retailer, and we want to show that. I am looking for a fresh look, double sided, modern card.. Open to any ideas or designs.

Target Market(s)

Looking to hit men/women 35-50.

Industry/Entity Type

Business

Contact Information for Business Card

Looking for a clean modern look. With that being said, we are wanting to highlight some of the awards that we have received ( Corvane Best 100 and top 16 National Premium, imagines linked). Also need website on card- www.buyvelmora.com, and follow us; facebook, instagram, twitter (small thumbnails work best for those 3) Would like website, social media info, and two awards on backside with some imagery (we are a furniture, mattress and appliance business) and then logo, name, title address on front side

Colors

Designer to choose colors to be used in the design.

Requirements
Must have
• Company name, address, website, two awards, social media ques
Should not have
• cartoons

```html
<!DOCTYPE html>
<html lang="en">
<head>
<meta charset="utf-8">
<title>Velmora Home Furnishings – Business Card</title>
<link rel="stylesheet" href="https://fonts.googleapis.com/css2?family=Roboto:wght@500;700;900&family=Roboto+Condensed:wght@700&family=Lato:wght@400;700&display=swap">
<style>
  :root {
    --backdrop: #8c6c47;
    --card: #ffffff;
    --brand-red: #b3252b;
    --brand-blue: #1f3f86;
    --ink: #222222;
    --wall: #e4e5e8;
    --wall-shade: #cfd0d3;
    --wood: #5a4840;
    --wood-dark: #46362f;
    --rug: #cbc6bf;
    --tile-one: #2a8fd6;
    --tile-two: #2d4f95;
    --tile-three: #b8417e;
    --badge-grey: #c9ccd2;
  }
  * { margin: 0; padding: 0; box-sizing: border-box; }
  html, body { width: 900px; height: 1200px; overflow: hidden; }
  body { background: var(--backdrop); position: relative; font-family: "Lato", sans-serif; color: var(--ink); }

  .card { position: absolute; left: 75px; width: 750px; background: var(--card); box-shadow: 0 6px 14px rgba(0,0,0,.35); overflow: hidden; }
  .card--back { top: 133px; height: 438px; }
  .card--front { top: 628px; height: 437px; }

  /* back side */
  .hero-photo {
    position: absolute; left: 0; top: 0; width: 750px; height: 360px;
    background:
      radial-gradient(ellipse 260px 120px at 260px 250px, rgba(70,54,47,.55), rgba(70,54,47,0) 100%),
      radial-gradient(ellipse 150px 130px at 640px 220px, rgba(70,54,47,.5), rgba(70,54,47,0) 100%),
      linear-gradient(180deg, var(--wall) 0%, var(--wall-shade) 45%, #a99c92 68%, var(--rug) 88%, #d9d6d2 100%);
  }
  .hero-curve { position: absolute; left: 0; top: 0; width: 750px; height: 438px; }

  .follow-band {
    position: absolute; left: 0; top: 375px; width: 148px; height: 40px;
    background: var(--brand-red); color: #fff;
    font-family: "Roboto Condensed", sans-serif; font-weight: 700; font-size: 19px;
    line-height: 40px; padding-left: 48px; letter-spacing: .2px;
  }
  .social-list { position: absolute; left: 149px; top: 374px; display: flex; gap: 5px; }
  .social-tile { width: 42px; height: 42px; border-radius: 9px; }
  .social-tile--one { background: var(--tile-one); }
  .social-tile--two { background: var(--tile-two); }
  .social-tile--three { background: var(--tile-three); }

  .award { position: absolute; }
  .award--ranking { left: 490px; top: 330px; width: 116px; height: 82px; background: var(--badge-grey); border-radius: 6px; }
  .award--seal { left: 622px; top: 334px; width: 88px; height: 88px; border-radius: 50%;
    background: radial-gradient(circle at 45% 40%, #d63a3a 0%, var(--brand-red) 70%, #8f1a1f 100%); }

  /* front side */
  .holder { position: absolute; left: 49px; top: 72px; }
  .holder__name { font-family: "Roboto Condensed", sans-serif; font-weight: 700; font-size: 35px; color: var(--brand-blue); letter-spacing: .8px; line-height: 1; }
  .holder__title { font-family: "Roboto", sans-serif; font-weight: 500; font-size: 20px; color: var(--brand-red); letter-spacing: .4px; margin-top: 4px; }

  .brand { position: absolute; right: 47px; top: 46px; text-align: right; }
  .brand__name { font-family: "Roboto", sans-serif; font-weight: 900; font-size: 86px; color: var(--brand-red); line-height: 1; letter-spacing: -1px; }
  .brand__tag { font-family: "Roboto", sans-serif; font-weight: 900; font-size: 27px; color: var(--brand-red); margin-top: 14px; }

  .divider { position: absolute; left: 49px; top: 291px; width: 653px; height: 2px; display: flex; }
  .divider .blue { width: 396px; background: var(--brand-blue); }
  .divider .red { flex: 1; background: var(--brand-red); }

  .contact { position: absolute; font-size: 19px; line-height: 29px; }
  .contact--left { left: 49px; top: 302px; }
  .contact--right { left: 446px; top: 302px; }
  .contact__row { display: flex; align-items: center; gap: 12px; }
  .contact__row--indent { padding-left: 34px; }
  .icon { width: 22px; height: 22px; flex: none; }

  .website { position: absolute; left: 0; width: 750px; top: 387px; display: flex; justify-content: center; align-items: center; gap: 9px;
    font-family: "Lato", sans-serif; font-weight: 700; font-size: 16px; letter-spacing: .2px; }
</style>
</head>
<body>

<section class="card card--back">
  <div class="hero-photo" role="img" aria-label="Bright bedroom with a dark wooden bed, nightstand, chest and dresser with mirror on a shaggy rug"></div>
  <svg class="hero-curve" viewBox="0 0 750 438" aria-hidden="true">
    <path d="M0 356 L440 356 C475 356 480 318 540 316 L750 312 L750 438 L0 438 Z" fill="#ffffff"/>
  </svg>

  <div class="follow-band">FOLLOW US</div>
  <div class="social-list">
    <span class="social-tile social-tile--one"></span>
    <span class="social-tile social-tile--two"></span>
    <span class="social-tile social-tile--three"></span>
  </div>

  <div class="award award--ranking" role="img" aria-label="Corvane Best 100 award badge"></div>
  <div class="award award--seal" role="img" aria-label="Best of the best award seal"></div>
</section>

<section class="card card--front">
  <div class="holder">
    <div class="holder__name">DORIAN HALE</div>
    <div class="holder__title">MANAGING DIRECTOR</div>
  </div>

  <div class="brand">
    <div class="brand__name">Velmora</div>
    <div class="brand__tag">Home Furnishings</div>
  </div>

  <div class="divider"><span class="blue"></span><span class="red"></span></div>

  <div class="contact contact--left">
    <div class="contact__row">
      <svg class="icon" viewBox="0 0 22 22" aria-hidden="true"><rect width="22" height="22" rx="4" fill="var(--brand-blue)"/><path d="M7 5c1 0 2 2 2 3s-1 1-1 2 2 4 4 4 1-1 2-1 3 1 3 2-1 2-3 2C9 17 5 12 5 8c0-2 1-3 2-3z" fill="#fff"/></svg>
      <span>555-014-2290</span>
    </div>
    <div class="contact__row">
      <svg class="icon" viewBox="0 0 22 22" aria-hidden="true"><rect width="22" height="22" rx="4" fill="var(--brand-blue)"/><rect x="5" y="7" width="12" height="9" fill="none" stroke="#fff" stroke-width="1.5"/><path d="M5 7l6 5 6-5" fill="none" stroke="#fff" stroke-width="1.5"/></svg>
      <span>info@buyvelmora.com</span>
    </div>
  </div>

  <div class="contact contact--right">
    <div class="contact__row">
      <svg class="icon" viewBox="0 0 22 22" aria-hidden="true"><rect width="22" height="22" rx="4" fill="var(--brand-red)"/><path d="M11 4a5 5 0 0 1 5 5c0 4-5 9-5 9s-5-5-5-9a5 5 0 0 1 5-5z" fill="#fff"/><circle cx="11" cy="9" r="2" fill="var(--brand-red)"/></svg>
      <span>Address goes here, street</span>
    </div>
    <div class="contact__row contact__row--indent"><span>Westbrook, Ashford-4120</span></div>
  </div>

  <div class="website">
    <svg class="icon" viewBox="0 0 22 22" aria-hidden="true"><g fill="none" stroke="var(--brand-red)" stroke-width="1.6"><circle cx="11" cy="11" r="9"/><ellipse cx="11" cy="11" rx="4" ry="9"/><path d="M2 11h18M4 6h14M4 16h14"/></g></svg>
    <span>WWW.BUYVELMORA.COM</span>
  </div>
</section>

</body>
</html>
```